Looking for a cool & simple business-card-design for digital agency

Hi!

We are a web agency that offers Reputation Management, Zorvik & Seo Services and software development. We like cool things, we like innovative styles.

We have uploaded our logo.

Project Deadline Extended Reason: Client does not want any designs with the colorful logo. Please send us submissions ONLY with the blac and white logo. What the client would like to see:1) Back of the card: is a silver logo on a black background2) front of the card with all the data, please use white background and black logo thank you Added Friday, May 8, 2015

Software

```html
<!DOCTYPE html>
<html lang="de">
<head>
<meta charset="utf-8">
<title>Nordwerk AG – Geschäftsausstattung</title>
<link rel="stylesheet" href="https://fonts.googleapis.com/css2?family=Open+Sans:wght@400;700&display=swap">
<style>
  :root {
    --stage: #5f5f5f;
    --paper: #ffffff;
    --ink: #1a1a1a;
    --ink-soft: #3a3a3a;
    --card-black: #0b0b0b;
    --silver: #d9d9d9;
    --band-dark: #111111;
    --band-light: #8a8a8a;
    --frame: #bdbdbd;
  }
  * { margin: 0; padding: 0; box-sizing: border-box; }
  html, body { width: 1200px; height: 750px; overflow: hidden; }
  body {
    position: relative;
    background: var(--stage);
    font-family: "Open Sans", Arial, sans-serif;
    color: var(--ink);
  }
  .sheet {
    position: absolute;
    background: var(--paper);
    box-shadow: 2px 3px 6px rgba(0,0,0,.35);
  }
  .brand { position: absolute; line-height: 1; }
  .brand__name {
    display: block;
    font-weight: 700;
    color: var(--ink);
    letter-spacing: .5px;
  }
  .brand__tagline {
    display: block;
    font-weight: 700;
    color: var(--ink);
    letter-spacing: 3px;
    margin-top: 3px;
  }
  .brand--silver .brand__name,
  .brand--silver .brand__tagline { color: var(--silver); }

  .mark-block {
    position: absolute;
    background: linear-gradient(135deg, #2b2b2b, #8c8c8c 55%, #1e1e1e);
  }
  .rule-band {
    position: absolute;
    height: 12px;
    background: linear-gradient(90deg, var(--band-dark), var(--band-light));
  }
  .address {
    position: absolute;
    font-weight: 700;
    font-size: 7px;
    line-height: 12px;
    color: var(--ink);
  }

  /* Letterhead */
  .letterhead { left: 43px; top: 27px; width: 492px; height: 695px; }
  .letterhead .brand { left: 24px; top: 18px; }
  .letterhead .brand__name { font-size: 22px; }
  .letterhead .brand__tagline { font-size: 10px; }
  .letterhead .mark-block { left: 12px; top: 632px; width: 62px; height: 56px; }
  .letterhead .rule-band { left: 86px; right: 0; top: 630px; }
  .letterhead .address { right: 14px; top: 657px; text-align: right; }

  /* Business card front */
  .card-front { left: 590px; top: 316px; width: 207px; height: 118px; overflow: hidden; }
  .card-front .brand { right: 10px; top: 7px; text-align: right; }
  .card-front .brand__name { font-size: 15px; }
  .card-front .brand__tagline { font-size: 7px; letter-spacing: 2px; margin-top: 2px; }
  .card-front .mark-block { left: 2px; top: 48px; width: 70px; height: 70px; }
  .title-band {
    position: absolute; left: 88px; right: 0; top: 48px; height: 11px;
    background: linear-gradient(90deg, #2a2a2a, #4a4a4a);
    color: #fff; font-size: 5px; display: flex; align-items: center;
    justify-content: space-between; padding: 0 6px;
  }
  .title-band__name { font-size: 6.5px; font-weight: 700; letter-spacing: .3px; }
  .contact-list {
    position: absolute; right: 6px; top: 64px; list-style: none;
    font-size: 5px; font-weight: 700; line-height: 8px; text-align: right;
  }
  .contact-list li { display: flex; align-items: center; justify-content: flex-end; gap: 3px; }
  .contact-icon { width: 5px; height: 5px; background: var(--ink); border-radius: 1px; display: inline-block; }
  .contact-icon--round { border-radius: 50%; }
  .card-front .address { right: 8px; top: 100px; font-size: 5px; line-height: 9px; text-align: right; }

  /* Business card back */
  .card-back { left: 814px; top: 318px; width: 206px; height: 116px; background: var(--card-black); overflow: hidden; }
  .card-back .mark-block { left: 8px; top: 14px; width: 90px; height: 96px; opacity: .55;
    background: linear-gradient(135deg, #111, #5a5a5a 55%, #111); }
  .card-back .brand { left: 71px; top: 42px; }
  .card-back .brand__name { font-size: 15px; }
  .card-back .brand__tagline { font-size: 7px; letter-spacing: 2px; margin-top: 2px; }

  /* Envelope */
  .envelope { left: 589px; top: 478px; width: 566px; height: 242px; }
  .envelope .brand { left: 18px; top: 15px; }
  .envelope .brand__name { font-size: 20px; }
  .envelope .brand__tagline { font-size: 9.5px; }
  .envelope .address { left: 18px; top: 55px; }
  .stamp-box { position: absolute; left: 503px; top: 16px; width: 49px; height: 66px; border: 1px solid var(--frame); }
  .envelope .mark-block { left: 18px; top: 178px; width: 60px; height: 56px; }
  .envelope .rule-band { left: 90px; right: 0; top: 178px; }
</style>
</head>
<body>
  <section class="sheet letterhead" aria-label="Briefbogen">
    <div class="brand">
      <span class="brand__name">Nordwerk AG</span>
      <span class="brand__tagline">DIGITALE STRATEGIEN</span>
    </div>
    <div class="mark-block" aria-hidden="true"></div>
    <div class="rule-band"></div>
    <p class="address">12TH FLOOR LANTERN RD.<br>SILOM, BANGRAK, BANGKOK 10500</p>
  </section>

  <section class="sheet card-front" aria-label="Visitenkarte Vorderseite">
    <div class="brand">
      <span class="brand__name">Nordwerk AG</span>
      <span class="brand__tagline">DIGITALE STRATEGIEN</span>
    </div>
    <div class="mark-block" aria-hidden="true"></div>
    <div class="title-band">
      <span class="title-band__role">Executive Director</span>
      <span class="title-band__name">DANIEL ROTH</span>
    </div>
    <ul class="contact-list">
      <li>(65) 91234567 <span class="contact-icon"></span></li>
      <li>droth@kelvamail.com <span class="contact-icon contact-icon--round"></span></li>
      <li>Kelva Studio Thailand <span class="contact-icon"></span></li>
      <li>kelvastudio <span class="contact-icon contact-icon--round"></span></li>
    </ul>
    <p class="address">12TH FLOOR LANTERN RD.<br>SILOM, BANGRAK, BANGKOK 10500</p>
  </section>

  <section class="sheet card-back" aria-label="Visitenkarte Rückseite">
    <div class="mark-block" aria-hidden="true"></div>
    <div class="brand brand--silver">
      <span class="brand__name">Nordwerk AG</span>
      <span class="brand__tagline">DIGITALE STRATEGIEN</span>
    </div>
  </section>

  <section class="sheet envelope" aria-label="Briefumschlag">
    <div class="brand">
      <span class="brand__name">Nordwerk AG</span>
      <span class="brand__tagline">DIGITALE STRATEGIEN</span>
    </div>
    <p class="address">12TH FLOOR LANTERN RD.<br>SILOM, BANGRAK, BANGKOK 10500</p>
    <div class="stamp-box" aria-hidden="true"></div>
    <div class="mark-block" aria-hidden="true"></div>
    <div class="rule-band"></div>
  </section>
</body>
</html>
```